Project Brightvale Remedies

We need a business/ logo card design for our company based out of Canada. We will be retailing cannibus products to our customers.
For colors I've found this online : https://www.pallortune.edu/shade-picker-output/?tones=70ff02,ff0270,ff4a02,02e1ff . We especially like the green and blue .
We would like our business card design to communicate modern medicine .

Target Market(s)

males 20-40 years

Industry/Entity Type

Health And Wellness

Contact Information for Business Card

Address is : 482 Marlow Ave E
Toronto, ON K3T 8R2
website: www.brightvaleremedies.com

Font styles to use
Serif

Requirements
Must have
• clear, easy to read logo
Nice to have
• contrasting colors
Should not have
• we want to stay away from marijuana leaf

```html
<!DOCTYPE html>
<html lang="en">
<head>
<meta charset="utf-8">
<title>Brightvale Remedies – Business Card</title>
<link rel="stylesheet" href="https://fonts.googleapis.com/css2?family=Tinos:wght@400&display=swap">
<style>
  :root {
    --backdrop: #e3e9ef;
    --card-white: #fbfcfd;
    --brand-green: #78b834;
    --brand-blue: #45b1de;
    --brand-blue-soft: #5cbde4;
    --text-white: #ffffff;
  }
  html, body {
    margin: 0;
    width: 1200px;
    height: 900px;
    overflow: hidden;
    background: var(--backdrop);
  }
  .business-card {
    position: absolute;
    left: 225px;
    top: 236px;
    width: 750px;
    height: 428px;
    border-radius: 16px;
    overflow: hidden;
    background: var(--card-white);
    box-shadow: 0 10px 30px rgba(40, 60, 80, 0.18);
    font-family: "Tinos", "Times New Roman", serif;
  }
  .decor-band {
    position: absolute;
    left: 0;
    right: 0;
    top: 240px;
    bottom: 0;
    background: linear-gradient(180deg, var(--brand-blue-soft) 0%, var(--brand-blue) 100%);
  }
  .brand-name {
    position: absolute;
    left: 64px;
    top: 62px;
    margin: 0;
    font-weight: 400;
    font-size: 40px;
    line-height: 48px;
    letter-spacing: 3px;
    text-transform: uppercase;
    color: var(--brand-green);
  }
  .holder {
    position: absolute;
    right: 58px;
    top: 54px;
    text-align: right;
  }
  .holder-name {
    margin: 0;
    font-size: 27px;
    line-height: 30px;
    color: var(--brand-green);
  }
  .holder-title {
    margin: 4px 0 0;
    font-size: 16px;
    color: var(--brand-blue);
  }
  .contact-list {
    position: absolute;
    right: 58px;
    top: 320px;
    margin: 0;
    padding: 0;
    list-style: none;
    text-align: right;
    color: var(--text-white);
    font-size: 16px;
  }
  .contact-list li {
    display: flex;
    justify-content: flex-end;
    align-items: center;
    gap: 10px;
    height: 26.5px;
  }
  .contact-icon {
    width: 16px;
    height: 16px;
  }
  .address {
    position: absolute;
    left: 34px;
    top: 374px;
    margin: 0;
    font-size: 16px;
    color: var(--text-white);
  }
</style>
</head>
<body>
  <article class="business-card">
    <div class="decor-band" role="img" aria-label="Decorative flowing band in blue and green across the lower card"></div>

    <h1 class="brand-name">Brightvale<br>Remedies</h1>

    <div class="holder">
      <p class="holder-name">Marcus Halden</p>
      <p class="holder-title">Managing Director</p>
    </div>

    <ul class="contact-list">
      <li>416-555-0192
        <svg class="contact-icon" viewBox="0 0 16 16" aria-hidden="true"><path fill="#fff" d="M1 5c0-2 3-3 7-3s7 1 7 3v1h-3V4.5H4V6H1Z M3 8l2-2h6l2 2v5H3Z"/><circle cx="8" cy="10" r="1.6" fill="var(--brand-blue)"/></svg>
      </li>
      <li>marcushalden@brightvale.com
        <svg class="contact-icon" viewBox="0 0 16 16" aria-hidden="true"><rect x="1" y="3" width="14" height="10" fill="#fff"/><path d="M1.5 3.5 8 9l6.5-5.5" fill="none" stroke="var(--brand-blue)" stroke-width="1.2"/></svg>
      </li>
      <li>www.brightvaleremedies.com
        <svg class="contact-icon" viewBox="0 0 16 16" aria-hidden="true"><g fill="none" stroke="#fff" stroke-width="1.3"><circle cx="8" cy="8" r="6.5"/><ellipse cx="8" cy="8" rx="3" ry="6.5"/><path d="M1.5 8h13M2.5 4.8h11M2.5 11.2h11"/></g></svg>
      </li>
    </ul>

    <p class="address">482 Marlow Ave E, Toronto, ON K3T 8R2</p>
  </article>
</body>
</html>
```